Website needed for a specialty chemical company!

We are looking for a new website design to replace our current site.
We are a woman and minority owned, specialty chemical company that specializes in environmentally safe products and chemicals, or what we like to call "green solutions".
Our clientele are mostly companies in the construction business, as our current products consist of asphalt release agents, tar/asphalt cleaners, concrete form release agents, concrete removers and environmentally safe detergents. If a special product is needed, our formulation team can also custom create chemicals and products for your industry or company.
We are looking for at least three pages total. A home page, a products page that lists our products and also provides additional product information and a contact us page.
Our current site is at: www.brovalin-solvex.com
This will give you a general idea of what type of content will be on our site.
We are very open to content ideas, pictures, colors and CREATIVITY.
We would like to stress that we are "environmentally friendly" and would like to use "earthy" tones and greens if possible.
We also prefer a more modern website design as opposed to something traditional. An example of a site design that we like is: http://www.tarivo.com/
The design does not have to follow this, this is just a site look and feel that we liked. :)
Updates
Target Market(s)
Construction Companies, Truckers
Industry/Entity Type
It Company
Coding
Coded - Design and coding required
Number of Pages Required
3 page
Font styles to use
Look and feel
Each slider illustrates characteristics of the customer's brand and the style your logo design should communicate.

```html
<!DOCTYPE html>
<html lang="en">
<head>
<meta charset="utf-8">
<title>Brovalin Solvex — Home</title>
<link rel="stylesheet" href="https://fonts.googleapis.com/css2?family=Open+Sans:wght@300;400;600;700&family=Open+Sans+Condensed:wght@700&display=swap">
<style>
:root{
  --page:#ffffff;
  --topbar:#5a5c57;
  --nav:#b5b8b1;
  --title-box:#2d3236;
  --olive:#76780f;
  --heading:#3d3d3d;
  --body-text:#9a9a9a;
  --footer:#1b1e20;
  --footer-head:#7f93a2;
  --footer-muted:#6e7f8b;
  --social:#4b4e51;
  --white:#ffffff;
}
*{box-sizing:border-box;margin:0;padding:0}
html,body{width:767px;height:1200px;overflow:hidden;background:var(--page)}
body{position:relative;font-family:"Open Sans",Arial,sans-serif}
.abs{position:absolute}

.top-bar{left:48px;top:39px;width:671px;height:41px;background:var(--topbar)}
.util{position:absolute;top:18px;font-size:5.5px;color:#a9aba6;letter-spacing:.2px;white-space:nowrap}
.util svg{vertical-align:middle}
.search{position:absolute;left:208px;top:14px;width:140px;height:14px;border:1px solid #9a9c97;font-size:7px;font-style:italic;color:#b9bbb6;padding:1px 4px}
.search-btn{position:absolute;left:349px;top:14px;width:35px;height:14px;background:#c4c6c1;color:var(--white);font-size:6.5px;font-weight:700;text-align:center;line-height:14px}

.main-nav{left:48px;top:80px;width:671px;height:54px;background:var(--nav)}
.main-nav a{position:absolute;top:14px;font-size:19.5px;font-weight:600;color:var(--white);text-decoration:none;letter-spacing:.3px;text-shadow:0 1px 2px rgba(0,0,0,.35)}

.hero{left:48px;top:134px;width:671px;height:315px;background:radial-gradient(ellipse at 30% 40%,#8a9a1e 0%,#556b14 35%,#3b4a12 70%,#2f3a10 100%);box-shadow:0 12px 14px -8px rgba(0,0,0,.35)}
.hero-title{left:87px;top:195px;width:589px;height:54px;background:var(--title-box);color:var(--white);font-family:"Open Sans Condensed","Arial Narrow",sans-serif;font-weight:700;font-size:48px;line-height:54px;text-align:center}
.hero-copy{left:170px;top:270px;width:428px;color:var(--white);font-weight:700;font-size:18px;line-height:23px;text-align:center}
.slide-dots{left:346px;top:408px;display:flex;gap:5px}
.slide-dots span{width:15px;height:15px;border:1.6px solid var(--white);border-radius:50%}

.feature{top:511px;width:220px;text-align:center}
.feature-symbol{display:block;margin:0 auto;width:113px;height:113px;border-radius:50%;background:var(--olive)}
.feature h2{margin-top:33px;font-size:18.5px;font-weight:600;color:var(--heading);letter-spacing:.3px}
.feature p{margin:20px auto 0;width:180px;font-size:15.5px;font-weight:300;line-height:22px;color:var(--body-text)}

.site-footer{left:48px;top:927px;width:671px;height:224px;background:var(--footer)}
.f-col{position:absolute;top:24px;font-size:9px;line-height:18.5px;color:var(--white)}
.f-col h3{font-family:"Open Sans Condensed","Arial Narrow",sans-serif;font-size:9.5px;font-weight:700;color:var(--footer-head);margin-bottom:1px}
.f-col .muted{color:var(--footer-muted);line-height:16px}
.f-col .muted b{color:var(--white);font-weight:600}
.store-badge{position:absolute;border:1px solid #cfd2d4;border-radius:4px}
.social{position:absolute;top:163px;width:33px;height:33px;border-radius:50%;background:var(--social)}
</style>
</head>
<body>

<header class="abs top-bar">
  <span class="util" style="left:94px;top:13px"><svg width="11" height="11" viewBox="0 0 24 24"><path d="M12 2l3 7 7 .6-5.3 4.6 1.7 7.3L12 17.8 5.6 21.5l1.7-7.3L2 9.6 9 9z" fill="none" stroke="#c9cbc6" stroke-width="1.6"/></svg> SAVED (0) &nbsp;|</span>
  <span class="util" style="left:154px;top:13px"><svg width="13" height="11" viewBox="0 0 26 22"><path d="M3 8h20l-2 13H5z M9 8a4 4 0 0 1 8 0" fill="#c9cbc6" stroke="#c9cbc6"/></svg> BAG (0)</span>
  <div class="search">Search</div>
  <div class="search-btn">SEARCH</div>
  <span class="util" style="left:397px">Contact Us &nbsp;&nbsp;&nbsp;|&nbsp;&nbsp;&nbsp; Gift Cards &nbsp;&nbsp;&nbsp;|&nbsp;&nbsp;&nbsp; Track Order &nbsp;&nbsp;&nbsp;|&nbsp;&nbsp;&nbsp; Sign Up</span>
</header>

<nav class="abs main-nav">
  <a style="left:88px">HOME</a>
  <a style="left:177px">PRODUCTS</a>
  <a style="left:304px">CONTACT US</a>
  <a style="left:456px">MY ACCOUNT</a>
</nav>

<section class="abs hero" role="img" aria-label="Soft-focus photograph of green grass"></section>
<h1 class="abs hero-title">Welcome to Brovalin Solvex™</h1>
<p class="abs hero-copy">Brovalin Solvex™ offers environmentally friendly products made from all natural and renewable resources. Our products are safe, and easy to use.</p>
<div class="abs slide-dots"><span></span><span></span><span></span><span></span></div>

<article class="abs feature" style="left:49px">
  <div class="feature-symbol" role="img" aria-label="Olive emblem symbolising safety"></div>
  <h2>SAFE TO USE</h2>
  <p>Brovalin products contain no dangerous chemicals or additives and are safe around you, your family, your pets and the environment.</p>
</article>

<article class="abs feature" style="left:269px">
  <div class="feature-symbol" role="img" aria-label="Olive emblem symbolising effectiveness"></div>
  <h2>EFFECTIVE</h2>
  <p>Brovalin products not only do their job, they do their job well.</p>
</article>

<article class="abs feature" style="left:490px">
  <div class="feature-symbol" role="img" aria-label="Olive emblem symbolising fair pricing"></div>
  <h2>ECONOMICALLY PRICED</h2>
  <p>Brovalin Solvex™ offers cost effective solutions on the job, around the home and for you.</p>
</article>

<footer class="abs site-footer">
  <div class="f-col" style="left:87px"><h3>SUPPORT</h3>FAQ<br>Feedback<br>Contact<br>How It Works<br>Testimonials</div>
  <div class="f-col" style="left:181px"><h3>COMPANY</h3>About Us<br>Partnership<br>Blog</div>
  <div class="f-col" style="left:294px"><h3>FUN STUFF</h3>Gift Certificates<br>Referrals<br>Training Center</div>
  <div class="f-col" style="left:399px"><h3>OUR MOBILE APPS</h3><span class="muted">Learn more about them <b>HERE</b><br>Or, here's some links to download them:</span></div>
  <div class="store-badge" style="left:398px;top:82px;width:89px;height:31px"></div>
  <div class="store-badge" style="left:498px;top:82px;width:89px;height:31px"></div>
  <span class="social" style="left:261px"></span>
  <span class="social" style="left:300px"></span>
  <span class="social" style="left:339px"></span>
  <span class="social" style="left:377px"></span>
</footer>

</body>
</html>
```